Lantern and Meadow Works: Problem to Solution Process

We need a powerpoint slide illustrating a process the begins with identifying a problem and proceed through various gates of potentially resolving the problem.
The attached file provides the steps a user must go through from point of recognizing they have a data need through resolving their problems are various stages.
This process is not yet in practice. It is a concept we are trying. We will use this slide to market the process while trying it with others.

Since the process is not yet in place, we need to visually communicate the theory we are implementing for users to quickly and easily understand. The resulting slide you are producing should tell the story of the user's path and the benefits for moving through this process. The slide with the process can include animation and / or videos to help demonstrate appropriately.
The largest benefit to the user is more immediate access to their data needs, to provide quicker insights and better decision making.
On the attached slide, the blue boxes are the processes we want to highlight. The text in the gray dotted boxes are intended to be informational for your purposes.
Each step 1- 4 should solve a user's problem. For example, if 100 problems are found, 50 should be resolved in step 1 and only 50 should move to step 2. Furthermore, only 30 should move to step 3 and 5 request should move to step 4. (Today, users go directly to step 4 for everything and it’s overwhelming to everyone!)

```html
<!DOCTYPE html>
<html lang="en">
<head>
<meta charset="utf-8">
<title>Lantern and Meadow Works: Problem to Solution Process</title>
<link rel="stylesheet" href="https://fonts.googleapis.com/css2?family=Montserrat:wght@800&family=Raleway:wght@400;500&display=swap">
<style>
:root{
  --page:#eeedee;
  --slide:#ffffff;
  --step:#4e7189;
  --gold:#a99b6b;
  --note:#f2f2f2;
  --ink:#2a2a2a;
  --muted:#8a8a8a;
  --dash:#a8a8a8;
}
*{margin:0;padding:0;box-sizing:border-box}
html,body{width:1200px;height:1200px;overflow:hidden;background:var(--page)}
.slide{position:absolute;left:0;top:262px;width:1200px;height:675px;background:var(--slide);font-family:"Raleway",sans-serif;color:var(--ink)}
.rule-top{position:absolute;left:81px;top:38px;width:1037px;height:3px;background:var(--gold)}
.rule-bottom{position:absolute;left:81px;top:612px;width:1037px;height:1px;background:#bdbdbd}
.wires{position:absolute;left:0;top:0;width:1200px;height:675px}
.step{position:absolute;background:var(--step);color:#fff;display:flex;flex-direction:column;align-items:center;justify-content:center;text-align:center}
.step-title{font-family:"Montserrat",sans-serif;font-weight:800;font-size:14px;line-height:1.3;letter-spacing:.3px}
.step-role{font-size:13.5px;font-weight:500;margin-top:5px;letter-spacing:.3px}
.step-start .step-role{display:none}
.step-start{font-size:10.5px;font-weight:500;line-height:1.25;letter-spacing:.3px}
.step-num{position:absolute;left:0;top:0;width:31px;height:30px;background:var(--gold);color:#fff;font-family:"Montserrat",sans-serif;font-weight:800;font-size:12px;display:flex;align-items:center;justify-content:center}
.note{position:absolute;background:var(--note);border-top:2px solid var(--step);font-size:9.6px;line-height:1.25;text-align:center;display:flex;align-items:center;justify-content:center;padding:0 10px;letter-spacing:.2px}
.label{position:absolute;font-size:10px;text-align:center;line-height:1.2;background:var(--slide);letter-spacing:.2px}
.footer-brand{position:absolute;left:46px;top:634px;display:flex;align-items:center;gap:7px;font-size:14px;letter-spacing:2.5px;text-transform:uppercase;color:var(--muted)}
.footer-brand .mark{width:16px;height:16px;background:var(--muted)}
.footer-conf{position:absolute;left:560px;top:638px;width:80px;text-align:center;font-size:9px}
.footer-copy{position:absolute;left:900px;top:638px;width:160px;text-align:center;font-size:8.5px;color:var(--muted)}
</style>
</head>
<body>
<main class="slide">
  <div class="rule-top"></div>

  <svg class="wires" viewBox="0 0 1200 675" aria-hidden="true">
    <defs>
      <marker id="head" viewBox="0 0 10 10" refX="9" refY="5" markerWidth="8" markerHeight="8" orient="auto">
        <path d="M0 0L10 5L0 10z" fill="#a99b6b"/>
      </marker>
    </defs>
    <g stroke="#a99b6b" stroke-width="1.6" fill="none" marker-end="url(#head)">
      <path d="M328 112V146"/>
      <path d="M328 254V309"/>
      <path d="M424 372H511"/>
      <path d="M328 434V487"/>
      <path d="M540 434V542H425"/>
      <path d="M705 372H742"/>
      <path d="M937 372H974"/>
      <path d="M996 310V84H938"/>
      <path d="M743 84H425"/>
    </g>
    <g stroke="#a8a8a8" stroke-width="1" stroke-dasharray="4 3" fill="none">
      <path d="M186 201H231"/>
      <path d="M186 372H231"/>
      <path d="M186 542H231"/>
      <path d="M609 254V310"/>
      <path d="M540 516H576"/>
      <path d="M822 434V487"/>
      <path d="M1030 434V487"/>
      <path d="M840 164V237H1093V164"/>
    </g>
  </svg>

  <div class="step step-start" style="left:231px;top:57px;width:193px;height:55px">User to communicate the<br>problem they are trying<br>to solve</div>

  <div class="step" style="left:743px;top:57px;width:194px;height:107px">
    <div class="step-title">Gain insights</div><div class="step-role">End User</div>
  </div>

  <div class="step" style="left:231px;top:147px;width:193px;height:107px">
    <span class="step-num">1</span>
    <div class="step-title">Self Service</div><div class="step-role">End User</div>
  </div>

  <div class="step" style="left:231px;top:310px;width:193px;height:124px">
    <span class="step-num">2</span>
    <div class="step-title">Super User Or<br>Problem Definition<br>Creation</div><div class="step-role">Super User</div>
  </div>

  <div class="step" style="left:512px;top:310px;width:193px;height:124px">
    <div class="step-title">Problem Solving<br>to Define problem</div><div class="step-role">Super User</div>
  </div>

  <div class="step" style="left:743px;top:310px;width:194px;height:124px">
    <span class="step-num">4</span>
    <div class="step-title">Project Design<br>&amp; Execute</div><div class="step-role">BI/EA teams</div>
  </div>

  <div class="step" style="left:975px;top:310px;width:193px;height:124px">
    <div class="step-title">Check Benefits</div><div class="step-role">BI teams</div>
  </div>

  <div class="step" style="left:231px;top:488px;width:193px;height:108px">
    <span class="step-num">3</span>
    <div class="step-title">Worked<br>within Agile</div><div class="step-role">BI teams</div>
  </div>

  <div class="note" style="left:1017px;top:57px;width:151px;height:107px">Reflection, feedback and training is needed to gain additional insights</div>
  <div class="note" style="left:35px;top:148px;width:151px;height:107px">Goal is for majority of needs are resolved with Self service by the end user.</div>
  <div class="note" style="left:512px;top:146px;width:193px;height:108px">If it is a large initiative to resolve, then a problem solving exercise needs to be completed to define the problem.</div>
  <div class="note" style="left:35px;top:295px;width:151px;height:156px">If the problem cannot by resolved by themselves, then they connect with a “super user” designation within the business. If they cannot solve the problem, they need to evaluate if it’s a large initiative or a small initiative to resolve.</div>
  <div class="note" style="left:35px;top:489px;width:151px;height:107px">The Business Intelligence team works in Agile teams. If it is a quick, small fix, then a user story is created in the appropriate BI team to quickly resolve it.</div>
  <div class="note" style="left:576px;top:487px;width:174px;height:109px">If the user needs data to finish problem solving exercise, then a request needs to be entered to quickly provide the data.</div>
  <div class="note" style="left:785px;top:487px;width:174px;height:109px">Once the problem is understood, the architecture design, data quality, data consistency and plan of how to solve the problem is created. Once aligned it is then executed</div>
  <div class="note" style="left:994px;top:487px;width:174px;height:109px">Regardless of the solution is resolved in steps 1, 2, 3, or 4, benefits and feedback is needed</div>

  <div class="label" style="left:268px;top:270px;width:120px">Results Not found</div>
  <div class="label" style="left:434px;top:390px;width:60px;background:none">Larger<br>Initiative/<br>New</div>
  <div class="label" style="left:248px;top:449px;width:160px">Existing, small or Quick Fix</div>
  <div class="label" style="left:440px;top:477px;width:96px;background:none;text-align:right">Need more data<br>to define problem</div>
  <div class="label" style="left:956px;top:193px;width:80px">Train &amp; Adopt</div>

  <div class="rule-bottom"></div>
  <div class="footer-brand"><span class="mark"></span>Lantern and Meadow Works</div>
  <div class="footer-conf">Confidential</div>
  <div class="footer-copy">© Lantern and Meadow Works</div>
</main>
</body>
</html>
```